I'm looking for strong image and design for the first book in a series titled "Bernard Whitcombe On A Voyage Through Our Convictions" subtitle "Finding a Footing in Living"; although it's about beliefs, I'm not look for an ethereal feel as the first book is about how our beliefs impact our actions and expectations. I'm a published philosopher and keen on branding my name for professional purposes hence the use of my name :) The book will initially be an e-book but I will follow up with a paperback soon afterwards. My website http://bernardwhitcombe-example.com/ may provide some help on me and my projects. Thanks, Bern

Target Market(s)

Graduates and corporate folk who tend to lose their way in the systems.

Logo Text

Bernard Whitcombe on Convictions

Font styles to use
Sans Serif

Colors

Designer to choose colors to be used in the design.

Requirements
Must have
• Needless to say, but impact.
Nice to have
• Strong colours
Should not have
• Religious imagery; the book is philosophical and leans into living in this world.

```html
<!DOCTYPE html>
<html lang="en">
<head>
<meta charset="utf-8">
<title>Bernard Whitcombe On A Voyage Through Our Convictions</title>
<link rel="stylesheet" href="https://fonts.googleapis.com/css2?family=Cormorant+SC:wght@500;600&display=swap">
<style>
  :root {
    --parchment: #f1e4c6;
    --parchment-deep: #e2cfa4;
    --ink-red: #7a1a12;
    --rule-brown: #8a5a2e;
    --gold-light: #e9c98a;
    --gold-mid: #c99a55;
    --gold-dark: #8e6228;
  }
  html, body {
    margin: 0;
    padding: 0;
    overflow: hidden;
    background: #ffffff;
  }
  .cover {
    position: relative;
    width: 841px;
    height: 1200px;
    overflow: hidden;
    background:
      radial-gradient(ellipse at 50% 45%, var(--parchment) 0%, var(--parchment) 45%, var(--parchment-deep) 100%);
    font-family: "Cormorant SC", "Times New Roman", serif;
    color: var(--ink-red);
    text-align: center;
  }
  .rule {
    position: absolute;
    height: 2px;
    background: var(--rule-brown);
  }
  .author {
    position: absolute;
    top: 40px;
    left: 0;
    width: 100%;
    margin: 0;
    font-size: 44px;
    font-weight: 600;
    letter-spacing: 1px;
  }
  .author-rule { top: 102px; left: 168px; width: 505px; }
  .artwork {
    position: absolute;
    top: 190px;
    left: 286px;
    width: 268px;
    height: 386px;
    box-sizing: border-box;
    border: 3px solid var(--gold-dark);
    padding: 12px;
    background: var(--gold-light);
  }
  .artwork-fill {
    width: 100%;
    height: 100%;
    border: 2px solid var(--gold-mid);
    box-sizing: border-box;
    background: radial-gradient(ellipse at 45% 45%, #f3dba6 0%, var(--gold-mid) 60%, var(--gold-dark) 100%);
  }
  .title {
    position: absolute;
    top: 665px;
    left: 0;
    width: 100%;
    margin: 0;
    font-size: 66px;
    font-weight: 600;
    line-height: 72px;
  }
  .title span { display: block; }
  .subtitle-rule-top { top: 948px; left: 246px; width: 349px; }
  .subtitle {
    position: absolute;
    top: 966px;
    left: 0;
    width: 100%;
    margin: 0;
    font-size: 48px;
    font-weight: 500;
  }
  .subtitle-rule-bottom { top: 1040px; left: 246px; width: 349px; }
</style>
</head>
<body>
  <main class="cover">
    <p class="author">Bernard Whitcombe</p>
    <div class="rule author-rule"></div>

    <figure class="artwork" style="margin:0">
      <div class="artwork-fill" role="img" aria-label="Golden-toned photograph of a seated thinking statue"></div>
    </figure>

    <h1 class="title">
      <span>Bernard Whitcombe</span>
      <span>On A Voyage Through</span>
      <span>Our Convictions</span>
    </h1>

    <div class="rule subtitle-rule-top"></div>
    <p class="subtitle">Finding a Footing in Living</p>
    <div class="rule subtitle-rule-bottom"></div>
  </main>
</body>
</html>
```